Design a styled business card for an intimacy and attachment psychologist

I am a Psychologist providing online therapy to patients across the United States. My work is interpersonal and emotion-focused, with an emphasis on the client-therapist relationship. My primary areas of work are very personal, including sexuality and gender, abuse and trauma, and grief and loss. My target audience will be adults of all ages 18+.
My business card should convey a warm and inviting feeling of professionalism that is also casual and comfortable.
The front should be fairly simple and professional, consisting of:
- My name, Dr. Rosalind Pembrook
- My title, Licensed Psycholigist
- My logo
On either the front or the back, my contact information should be listed:
- ros@drrospembrook.example
- 555.014.7789
- drrospembrook.example
On the rear, I would like a description of the areas that I specialize in. This can be formatted in any way that appears stylistically interesting.
Individual and Couples
Relationships and Infidelity
Sexual Health & Aging
Gender Identity & Sexual Orientation
Abuse and Trauma
Sexual Compulsivity & Addiction
Sexual Dysfunction
Target Market(s)
My target audience will be adults of all ages 18+.
Industry/Entity Type
Psychology
Contact Information for Business Card
The front should be fairly simple and professional, consisting of: - My name, Dr. Rosalind Pembrook - My title, Licensed Psycholigist - My logo On either the front or the back, my contact information should be listed: - ros@drrospembrook.example - 555.014.7789 - drrospembrook.example On the rear, I would like a description of the areas that I specialize in. This can be formatted in any way that appears stylistically interesting. Individual and Couples Relationships and Infidelity Sexual Health & Aging Gender Identity & Sexual Orientation Abuse and Trauma Sexual Compulsivity & Addiction Sexual Dysfunction

```html
<!DOCTYPE html>
<html lang="en">
<head>
<meta charset="utf-8">
<title>Dr. Rosalind Pembrook — Business Card</title>
<link href="https://fonts.googleapis.com/css2?family=Montserrat:wght@400;500;700;800&display=swap" rel="stylesheet">
<style>
  :root {
    --ink: #2e2a4f;
    --ink-soft: #47426b;
    --text-grey: #5a5a63;
    --card-front: #ffffff;
    --card-back: #efeff1;
    --backdrop: #d9d9dc;
    --mark-mint: #86cdb9;
  }
  * { box-sizing: border-box; margin: 0; padding: 0; }
  html, body {
    width: 1200px; height: 1200px; overflow: hidden;
    background: var(--backdrop);
    font-family: "Montserrat", sans-serif;
  }
  .stage {
    width: 1200px; height: 1200px;
    display: flex; flex-direction: column; align-items: center; justify-content: center;
    gap: 56px;
  }
  .card {
    width: 900px; height: 514px;
    border-radius: 26px;
    position: relative;
    box-shadow: 0 10px 28px rgba(0,0,0,0.12);
  }
  .card--specialties { background: var(--card-front); }
  .card--contact { background: var(--card-back); }

  /* brand lockup */
  .brand { display: flex; align-items: center; gap: 22px; }
  .brand__dot {
    width: 110px; height: 110px; border-radius: 50%;
    background: var(--mark-mint); flex: none;
  }
  .brand__name {
    color: var(--ink); font-weight: 500; font-size: 40px;
    line-height: 1.05; letter-spacing: 0.5px;
  }

  /* specialties side */
  .card--specialties .brand { position: absolute; left: 235px; top: 70px; }
  .specialty-tag {
    position: absolute; left: 280px; top: 230px;
    background: var(--ink); color: #fff;
    font-weight: 800; font-size: 26px;
    padding: 10px 36px; border-radius: 30px;
  }
  .specialty-list {
    position: absolute; list-style: none;
    color: var(--text-grey); font-size: 21px; line-height: 1.35; letter-spacing: 0.4px;
  }
  .specialty-list li::before, .specialty-list--right li::after {
    content: ""; display: inline-block; width: 8px; height: 8px;
    border-radius: 50%; background: var(--ink-soft); vertical-align: middle;
  }
  .specialty-list--left { left: 80px; top: 340px; }
  .specialty-list--left li::before { margin-right: 10px; }
  .specialty-list--right { right: 80px; top: 320px; text-align: right; }
  .specialty-list--right li::before { display: none; }
  .specialty-list--right li::after { margin-left: 10px; }

  /* contact side */
  .card--contact .brand {
    position: absolute; left: 90px; top: 0; bottom: 0;
    flex-direction: column; justify-content: center; gap: 26px; width: 340px;
  }
  .card--contact .brand__name { text-align: center; font-size: 42px; }
  .divider {
    position: absolute; left: 440px; top: 90px; bottom: 90px;
    width: 3px; background: var(--ink);
  }
  .contact { position: absolute; left: 490px; top: 96px; color: var(--ink); }
  .contact__name { font-weight: 800; font-size: 30px; }
  .contact__title { font-size: 22px; margin-top: 6px; color: var(--ink-soft); }
  .contact__address { font-size: 22px; margin-top: 22px; line-height: 1.35; color: var(--ink-soft); }
  .contact__lines { list-style: none; margin-top: 22px; font-size: 22px; color: var(--ink-soft); }
  .contact__lines li { display: flex; align-items: center; gap: 14px; line-height: 1.55; }
  .contact__lines svg { width: 20px; height: 20px; fill: var(--ink); flex: none; }
</style>
</head>
<body>
<main class="stage">

  <section class="card card--specialties">
    <div class="brand">
      <span class="brand__dot"></span>
      <span class="brand__name">Dr. Rosalind<br>Pembrook</span>
    </div>
    <div class="specialty-tag">I am Specialize in</div>
    <ul class="specialty-list specialty-list--left">
      <li>Individual and Couples</li>
      <li>Relationships and Infidelity</li>
      <li>Sexual Compulsivity &amp; Addiction</li>
      <li>Gender Identity &amp; Sexual Orientation</li>
    </ul>
    <ul class="specialty-list specialty-list--right">
      <li>Sexual Health &amp; Aging</li>
      <li>Sexual Dysfunction</li>
      <li>Sexual Dysfunction</li>
    </ul>
  </section>

  <section class="card card--contact">
    <div class="brand">
      <span class="brand__dot"></span>
      <span class="brand__name">Dr. Rosalind<br>Pembrook</span>
    </div>
    <div class="divider"></div>
    <div class="contact">
      <div class="contact__name">Dr. Rosalind Pembrook</div>
      <div class="contact__title">Licensed Psycholigist</div>
      <div class="contact__address">4410 Alder Lane<br>Fernbrook Maine 04021</div>
      <ul class="contact__lines">
        <li>
          <svg viewBox="0 0 24 24" aria-hidden="true"><path d="M6.6 10.8a15.1 15.1 0 0 0 6.6 6.6l2.2-2.2a1 1 0 0 1 1-.25 11.4 11.4 0 0 0 3.6.57 1 1 0 0 1 1 1V20a1 1 0 0 1-1 1A17 17 0 0 1 3 4a1 1 0 0 1 1-1h3.5a1 1 0 0 1 1 1c0 1.25.2 2.45.57 3.57a1 1 0 0 1-.25 1z"/></svg>
          555.014.7789
        </li>
        <li>
          <svg viewBox="0 0 24 24" aria-hidden="true"><path d="M2 5h20v14H2z M2 5l10 8 10-8" /></svg>
          ros@drrospembrook.example
        </li>
        <li>
          <svg viewBox="0 0 24 24" aria-hidden="true"><path d="M12 2a10 10 0 1 0 0 20 10 10 0 0 0 0-20zm6.9 6h-2.9a15.7 15.7 0 0 0-1.4-3.6A8 8 0 0 1 18.9 8zM12 4c.8 1.2 1.5 2.5 1.9 4h-3.8c.4-1.5 1.1-2.8 1.9-4zM4.3 14a8 8 0 0 1 0-4h3.4a16.5 16.5 0 0 0 0 4zm.8 2h2.9c.3 1.3.8 2.5 1.4 3.6A8 8 0 0 1 5.1 16zM8 8H5.1a8 8 0 0 1 4.3-3.6C8.8 5.5 8.3 6.7 8 8zm4 12c-.8-1.2-1.5-2.5-1.9-4h3.8c-.4 1.5-1.1 2.8-1.9 4zm2.3-6H9.7a14.7 14.7 0 0 1 0-4h4.6a14.7 14.7 0 0 1 0 4zm.3 5.6c.6-1.1 1.1-2.3 1.4-3.6h2.9a8 8 0 0 1-4.3 3.6zm1.7-5.6a16.5 16.5 0 0 0 0-4h3.4a8 8 0 0 1 0 4z"/></svg>
          www.drrospembrook.example
        </li>
      </ul>
    </div>
  </section>

</main>
</body>
</html>
```